Business Card/ Banner/ Logo/ Shirt design for (Harbour total Health Club) already have a rough idea

Hi,

I designed the business Harbour Total Health Club to create an environment where people could walk in to and feel at home, a place they could love and talk to all their friends about. I run group classes, personal training and gym activities however my interaction with clients is on a much deeper level and I help them with inspiration and life coaching improving their life with a holistic approach. I want harbour to become global and be seen as the benchmark for professionalism, yet compassion, wellness and an ora of unconditional love and care for its clients and members. I created Harbour so that people could experience life, energy and passion and begin to really love, enjoy, thrive, create and embrace their dreams and follow them.

I have made a logo that I feel best captures this mission however I used it using Microsoft word and paint so in terms of using it as a template the resolution could become distorted.

So I really reach out to the designers that want to be part of something passionate and help the harbour logo, design and vision come to physical form.

I like the logo I have created and I like purple as a feature colour, however I am open to any alterations or tweaks that your designer prowess may feel that will fit with the mission, description and vision the Harbour Total Health Club will carry of to invigorate the lives of millions.

I am also looking for a shirt design that looks professional and modern as well as fresh with life and credibility

I appreciate your time, thank you and I would love to have your inspired ideas come to life :)

Regards Tomas

If you need to contact me

Email tomasbrennick@mailvale.net
Mob 0477 213 496

Industry/Entity Type

Life Coaching

Contact Information for Business Card

Harbour Total Health Club, fitness studio and wellness centre

Logo styles of interest
Emblem Logo
Pictorial/Combination Logo
Abstract Logo
Character Logo
Wordmark Logo
Lettermark Logo
Requirements
Nice to have
• Purple, original "H" logo
Tag line "the essence of energy"

```html
<!DOCTYPE html>
<html lang="en">
<head>
<meta charset="utf-8">
<title>Harbour Total Health Club – Business Cards</title>
<link rel="stylesheet" href="https://fonts.googleapis.com/css2?family=Roboto:ital,wght@0,300;0,400;0,700;1,300&display=swap">
<style>
  :root {
    --purple-deep: #552a74;
    --purple-mid: #7d4c9e;
    --purple-light: #9a6cbb;
    --paper: #ffffff;
    --ground: #ebe8ee;
    --rule-light: rgba(255, 255, 255, 0.7);
  }
  * { box-sizing: border-box; margin: 0; padding: 0; }
  html, body {
    width: 1200px;
    height: 900px;
    overflow: hidden;
    background: var(--ground);
    font-family: "Roboto", Arial, sans-serif;
  }
  .canvas {
    position: relative;
    width: 1200px;
    height: 900px;
  }

  /* Front card */
  .card-front {
    position: absolute;
    left: 40px;
    top: 115px;
    width: 422px;
    height: 725px;
    background: var(--paper);
    box-shadow: 0 6px 18px rgba(60, 30, 80, 0.18);
  }
  .card-front .frame {
    position: absolute;
    inset: 28px;
    border: 1px solid var(--purple-mid);
  }
  .brand-block {
    position: absolute;
    left: 28px;
    right: 28px;
    top: 150px;
    display: flex;
    flex-direction: column;
    align-items: center;
    gap: 26px;
  }
  .brand-square {
    width: 96px;
    height: 96px;
    background: var(--purple-mid);
  }
  .brand-name {
    color: var(--purple-deep);
    font-weight: 700;
    font-size: 54px;
    line-height: 1.02;
    text-align: center;
    letter-spacing: -1px;
  }
  .tagline {
    position: absolute;
    left: 28px;
    right: 28px;
    bottom: 38px;
    text-align: center;
    color: var(--purple-mid);
    font-weight: 300;
    font-style: italic;
    font-size: 22px;
    line-height: 1;
  }

  /* Back card */
  .card-back {
    position: absolute;
    left: 680px;
    top: 375px;
    width: 280px;
    height: 485px;
    background: var(--purple-deep);
    box-shadow: 0 6px 18px rgba(40, 15, 60, 0.25);
  }
  .card-back .frame {
    position: absolute;
    inset: 18px;
    border: 1px solid var(--rule-light);
  }
  .back-name {
    position: absolute;
    left: 18px;
    right: 18px;
    top: 40px;
    text-align: center;
    color: var(--paper);
    font-weight: 700;
    font-size: 22px;
    line-height: 1.1;
  }
  .contact-list {
    position: absolute;
    left: 0;
    right: 0;
    top: 158px;
    display: flex;
    flex-direction: column;
    align-items: center;
    gap: 2px;
    list-style: none;
    color: var(--paper);
    font-weight: 400;
    font-size: 14px;
  }
  .contact-list li {
    display: flex;
    align-items: center;
    gap: 4px;
  }
  .contact-list svg { width: 14px; height: 14px; fill: var(--paper); }

  /* Standalone brand name (top right) */
  .brand-standalone {
    position: absolute;
    left: 850px;
    top: 60px;
    width: 300px;
    color: var(--purple-mid);
    font-weight: 700;
    font-size: 40px;
    line-height: 1.05;
    text-align: center;
  }
</style>
</head>
<body>
<main class="canvas">

  <section class="card-front" aria-label="Business card front">
    <div class="frame"></div>
    <div class="brand-block">
      <div class="brand-square" aria-hidden="true"></div>
      <h1 class="brand-name">Harbour<br>Total Health<br>Club</h1>
    </div>
    <p class="tagline">the essence of energy</p>
  </section>

  <section class="card-back" aria-label="Business card back">
    <div class="frame"></div>
    <p class="back-name">Harbour<br>Total Health Club</p>
    <ul class="contact-list">
      <li>
        <svg viewBox="0 0 24 24" aria-hidden="true"><path d="M6.6 10.8a15.1 15.1 0 0 0 6.6 6.6l2.2-2.2a1 1 0 0 1 1-.25 11.4 11.4 0 0 0 3.6.57 1 1 0 0 1 1 1V20a1 1 0 0 1-1 1A17 17 0 0 1 3 4a1 1 0 0 1 1-1h3.5a1 1 0 0 1 1 1c0 1.25.2 2.45.57 3.570a1 1 0 0 1-.25 1z"/></svg>
        <span>0477213496</span>
      </li>
      <li>
        <svg viewBox="0 0 24 24" aria-hidden="true"><path d="M2 5h20v14H2z M3.5 6.5 12 13l8.5-6.5" fill="none" stroke="#fff" stroke-width="1.6"/></svg>
        <span>tomasbrennick@mailvale.net</span>
      </li>
    </ul>
  </section>

  <p class="brand-standalone">Harbour<br>Total Health Club</p>

</main>
</body>
</html>
```